Business Card Design

RETAIL HIGH END CONTEMPORARY WOMEN'S CLOTHING STORE
MODERN, SIMPLE, CLEAN, COOL

WE ARE ALL ABOUT NY and CALIF STYLE.... CLASSY but EDGY..
COOLEST DENIM , Trendsetting, NEUTRAL Pallettes,
Collections : Fig and Stone, Dorian Vesk, PMW, K47, QTB
Don't need names of collections on card. thats just good info
for designer of card.

WOULD LIKE THE FONT TO BE INTERESTING, but CLEAN
We are on facebook daily with photos of outfits we put together
which you can look up and friend us.... MolvaHarbor
Also on instagram .
Open to options on color and size, but need cool and fresh.

Contact Information for Business Card

DELLA 5417 Larkmoor Rd. #309 Ember Court Arcade..Va. Beach, Va. 23987
Phone 757.386.5049 Fax 757.386-2613 EMAIL..DELLAMODE@QUILLBOX.COM

```html
<!DOCTYPE html>
<html lang="en">
<head>
<meta charset="utf-8">
<title>Business Card</title>
<link rel="stylesheet" href="https://fonts.googleapis.com/css2?family=Source+Sans+3:wght@400;600&family=PT+Sans+Narrow:wght@400;700&display=swap">
<style>
  :root {
    --stage: #05070a;
    --card: #d1d2d6;
    --ink: #111214;
    --rule: #8a8c90;
    --blue-light: #0fb0ff;
    --blue-mid: #0a8fef;
    --blue-deep: #0a5fd6;
    --grey-light: #a4a6aa;
    --grey-dark: #4c4e52;
  }
  html, body {
    margin: 0;
    padding: 0;
    width: 1200px;
    height: 900px;
    overflow: hidden;
    background: var(--stage);
  }
  .canvas {
    position: relative;
    width: 1200px;
    height: 900px;
    background: var(--stage);
  }
  .card {
    position: absolute;
    left: 202.5px;
    top: 139.5px;
    width: 774px;
    height: 523.5px;
    background: var(--card);
    overflow: hidden;
  }
  .card-graphics {
    position: absolute;
    inset: 0;
    width: 100%;
    height: 100%;
  }
  .logo-box {
    position: absolute;
    left: 117px;
    top: 37.5px;
    width: 123px;
    height: 87px;
    border: 1.5px solid #2a2b2e;
    display: flex;
    align-items: center;
    justify-content: center;
    font-family: "Source Sans 3", sans-serif;
    font-size: 42px;
    color: var(--ink);
  }
  .company-name {
    position: absolute;
    left: 33px;
    top: 145px;
    margin: 0;
    font-family: "Source Sans 3", sans-serif;
    font-weight: 400;
    font-size: 58px;
    letter-spacing: -1.5px;
    color: var(--ink);
    line-height: 1;
  }
  .contact {
    position: absolute;
    font-family: "PT Sans Narrow", sans-serif;
    color: var(--ink);
    margin: 0;
  }
  .contact-address {
    left: 12px;
    top: 470px;
    width: 196px;
    font-size: 12.5px;
    font-weight: 700;
    line-height: 21px;
    letter-spacing: -0.2px;
  }
  .contact-phone {
    left: 232px;
    top: 467px;
    font-family: "Source Sans 3", sans-serif;
    font-size: 16px;
    line-height: 21px;
  }
  .contact-email {
    left: 412px;
    top: 458px;
    width: 200px;
    text-align: center;
    font-size: 13.5px;
    line-height: 21px;
  }
</style>
</head>
<body>
<main class="canvas">
  <section class="card">
    <svg class="card-graphics" viewBox="0 0 516 349" preserveAspectRatio="none" aria-hidden="true">
      <defs>
        <linearGradient id="grey-panel" x1="0" y1="0" x2="1" y2="0">
          <stop offset="0" stop-color="var(--grey-light)"/>
          <stop offset="1" stop-color="var(--grey-dark)"/>
        </linearGradient>
        <linearGradient id="blue-band" x1="0" y1="0" x2="1" y2="1">
          <stop offset="0" stop-color="var(--blue-light)"/>
          <stop offset="0.55" stop-color="var(--blue-mid)"/>
          <stop offset="1" stop-color="var(--blue-deep)"/>
        </linearGradient>
        <linearGradient id="blue-bar" x1="0" y1="0" x2="1" y2="0">
          <stop offset="0" stop-color="var(--blue-light)"/>
          <stop offset="1" stop-color="var(--blue-deep)"/>
        </linearGradient>
      </defs>
      <polygon class="grey-panel-upper" points="308,0 516,0 516,287" fill="url(#grey-panel)"/>
      <polygon class="blue-band-upper" points="258,0 308,0 516,287 516,232" fill="url(#blue-band)"/>
      <polygon class="grey-panel-lower" points="420,349 487,262 516,290 516,349" fill="url(#grey-panel)"/>
      <polygon class="blue-band-lower" points="393,349 478,246 488,261 421,349" fill="url(#blue-band)"/>
      <rect class="accent-bar" x="28" y="287" width="51" height="5.5" fill="url(#blue-bar)"/>
      <rect class="accent-bar" x="171" y="280" width="52" height="5.5" fill="url(#blue-bar)"/>
      <rect class="accent-bar" x="314" y="280" width="54" height="5.5" fill="url(#blue-bar)"/>
      <line class="divider" x1="141" y1="297" x2="141" y2="349" stroke="var(--rule)" stroke-width="0.8"/>
      <line class="divider" x1="275" y1="297" x2="275" y2="349" stroke="var(--rule)" stroke-width="0.8"/>
    </svg>

    <div class="logo-box">Logo</div>
    <h1 class="company-name">Company name</h1>

    <p class="contact contact-address">DELLA 5417 Larkmoor Rd. #309 Ember<br>Court Arcade..Va. Beach, Va. 23987</p>
    <p class="contact contact-phone">Phone 757.386.5049<br>&nbsp;Fax 757.386-2613</p>
    <p class="contact contact-email">EMAIL..<br>DELLAMODE@QUILLBOX.COM</p>
  </section>
</main>
</body>
</html>
```